Can you create a Business Card based on the Logo you designed.

See example and would like to see other examples.

Trying to keep it very clean with a focus on the logo and name.

```html
<!DOCTYPE html>
<html lang="en">
<head>
<meta charset="utf-8">
<title>Fieldora Business Card</title>
<link rel="stylesheet" href="https://fonts.googleapis.com/css2?family=Open+Sans:wght@400;700&display=swap">
<style>
  :root {
    --page-bg: #2a2a2c;
    --card-bg: #1a1a1a;
    --card-edge: #101010;
    --emboss: #222222;
    --green-deep: #11894a;
    --green-bright: #52b847;
    --accent-orange: #f39a37;
    --text-light: #f2f2f2;
  }
  * { box-sizing: border-box; margin: 0; padding: 0; }
  html, body {
    width: 1200px; height: 780px; overflow: hidden;
    background: var(--page-bg);
    font-family: "Open Sans", Arial, sans-serif;
  }
  .card-set {
    display: flex; gap: 40px;
    padding: 235px 40px;
  }
  .card {
    width: 540px; height: 310px;
    background: var(--card-bg);
    border-radius: 26px;
    box-shadow: 0 6px 0 var(--card-edge), 0 18px 40px rgba(0,0,0,.45);
    position: relative; overflow: hidden;
  }
  /* front */
  .card-front { display: flex; align-items: center; padding: 0 36px 0 40px; }
  .brand { display: flex; align-items: center; gap: 10px; width: 230px; }
  .brand-dot { width: 22px; height: 22px; border-radius: 50%; background: var(--accent-orange); flex: none; }
  .brand-name { font-size: 44px; font-weight: 700; color: var(--green-deep); letter-spacing: -0.5px; }
  .divider { width: 2px; height: 150px; background: var(--green-deep); margin: 0 26px 0 10px; flex: none; }
  .contact-block { color: var(--text-light); }
  .person-name { font-size: 23px; font-weight: 700; text-transform: uppercase; letter-spacing: .5px; line-height: 1.1; }
  .person-name .first { color: var(--green-deep); }
  .person-name .last { color: var(--green-bright); }
  .person-title { font-size: 15px; margin: 4px 0 16px; }
  .contact-list { list-style: none; font-size: 14px; line-height: 1.75; }
  .contact-list li { display: flex; align-items: center; gap: 8px; }
  .contact-list svg { width: 13px; height: 13px; flex: none; }
  /* back */
  .card-back { display: flex; align-items: center; justify-content: center; }
  .brand-emboss {
    font-size: 110px; font-weight: 700; color: var(--emboss);
    letter-spacing: -2px;
  }
</style>
</head>
<body>
<main class="card-set">
  <section class="card card-front" aria-label="Business card front">
    <div class="brand">
      <span class="brand-dot"></span>
      <span class="brand-name">Fieldora</span>
    </div>
    <div class="divider"></div>
    <div class="contact-block">
      <h1 class="person-name"><span class="first">Marlon</span> <span class="last">Keeler</span></h1>
      <p class="person-title">Chief Executive Officer</p>
      <ul class="contact-list">
        <li>
          <svg viewBox="0 0 16 16" aria-hidden="true"><path fill="#52b847" d="M3.5 1.5l2.6 0 1 3.4-1.6 1.3a8 8 0 0 0 4.3 4.3l1.3-1.6 3.4 1v2.6c0 .8-.7 1.5-1.5 1.5A12.5 12.5 0 0 1 2 3c0-.8.7-1.5 1.5-1.5z"/></svg>
          +1 (555) 014-2278
        </li>
        <li>
          <svg viewBox="0 0 16 16" aria-hidden="true"><rect x="1" y="3" width="14" height="10" rx="1.5" fill="#52b847"/><path d="M1.5 4l6.5 5 6.5-5" stroke="#1a1a1a" stroke-width="1.4" fill="none"/></svg>
          CEO@fieldora.com
        </li>
        <li>
          <svg viewBox="0 0 16 16" aria-hidden="true"><circle cx="8" cy="8" r="6.5" fill="none" stroke="#52b847" stroke-width="1.6"/><ellipse cx="8" cy="8" rx="2.6" ry="6.5" fill="none" stroke="#52b847" stroke-width="1.3"/><path d="M1.5 8h13" stroke="#52b847" stroke-width="1.3"/></svg>
          www.fieldora.com
        </li>
      </ul>
    </div>
  </section>
  <section class="card card-back" aria-label="Business card back">
    <span class="brand-emboss">Fieldora</span>
  </section>
</main>
</body>
</html>
```